Life Coaching and Personal Development Business. Needs Business Card with Logo

We are a Life Coaching and Personal Development Business based in Melbourne, Victoria. We specialise in assisting Individuals who find themselves at cross roads due to career, relationships or just life experiences that are preventing them from having extraordinary lives in happiness, finance or relationships or just being disconnected from a sense of purpose. Our motto is "we help you get there".
Updates

Reason: I am awaiting final concepts from a couple of designers

Reason: Deadline passed so now would like to see more options.

Target Market(s)

Individuals who want to move through the cross roads and who are aware that they require help to do so. They are seeking happy, for filing lives through all aspects career, relationships, family and finance

Industry/Entity Type

Finance

Font styles to use
Script

Requirements
Must have
• logo which is representative of moving forward
Business Name: RV Bright Harbour
ABN: 5836071924

I do not have a preference with colour but I do not want red orange or green

Should not have
• The card must not be to busy.

```html
<!DOCTYPE html>
<html lang="en">
<head>
<meta charset="utf-8">
<title>RV Bright Harbour – Business Card</title>
<link rel="stylesheet" href="https://fonts.googleapis.com/css2?family=Lobster&family=Questrial&display=swap">
<style>
  :root {
    --pink: #e0246f;
    --pink-deep: #d21c62;
    --pink-bright: #ea2f7c;
    --white: #ffffff;
    --backdrop: #ebe8e4;
    --stone-lilac: #b5bcd9;
    --stone-blush: #f6c9c9;
    --stone-rose: #f3dada;
    --stone-magenta: #c8166a;
  }
  * { margin: 0; padding: 0; box-sizing: border-box; }
  html, body { width: 1200px; height: 900px; overflow: hidden; }
  body {
    background: var(--backdrop);
    position: relative;
    font-family: "Questrial", "Century Gothic", sans-serif;
  }

  .card {
    position: absolute;
    top: 120px;
    width: 380px;
    height: 660px;
    box-shadow: 0 6px 18px rgba(0,0,0,0.18);
    overflow: hidden;
  }

  /* Front */
  .card-front { left: 200px; background: var(--white); }
  .brand {
    position: absolute; top: 34px; left: 0; width: 100%;
    display: flex; flex-direction: column; align-items: center;
  }
  .brand-circle {
    width: 84px; height: 84px; border-radius: 50%;
    border: 5px solid var(--pink);
  }
  .brand-name {
    margin-top: 10px;
    font-family: "Lobster", cursive;
    font-size: 36px; color: var(--pink); line-height: 1;
  }
  .contact {
    position: absolute; top: 222px; left: 0; width: 100%;
    text-align: center; color: var(--pink);
    font-size: 17px; line-height: 1.35;
  }
  .contact-name { font-weight: bold; font-size: 19px; }
  .contact-role { margin-bottom: 28px; }
  .motto {
    position: absolute; top: 432px; left: 0; width: 100%;
    text-align: center;
    font-family: "Lobster", cursive;
    font-size: 25px; color: var(--pink);
  }
  .stones {
    position: absolute; left: 0; bottom: 0; width: 100%; height: 180px;
  }

  /* Back */
  .card-back {
    left: 620px;
    background: linear-gradient(160deg, var(--pink-bright), var(--pink-deep));
    display: flex; flex-direction: column; align-items: center; justify-content: center;
  }
  .card-back .brand-circle { width: 104px; height: 104px; border-color: var(--white); }
  .card-back .brand-name { color: var(--white); font-size: 42px; margin-top: 12px; }
</style>
</head>
<body>

  <section class="card card-front">
    <div class="brand">
      <div class="brand-circle"></div>
      <div class="brand-name">RV Bright Harbour</div>
    </div>

    <div class="contact">
      <div class="contact-name">Lauren Ashby</div>
      <div class="contact-role">Life Coach</div>
      <div>M: 04 5183 2604</div>
      <div>E: lauren@brightharbour.com.au</div>
      <div>PO Box 4129 Sandringham VIC 3191</div>
    </div>

    <div class="motto">“We help you get there”</div>

    <svg class="stones" role="img" aria-label="Illustration of a path of glossy stepping stones in lilac, blush and magenta rising into the distance" viewBox="0 0 380 180" preserveAspectRatio="none">
      <defs>
        <linearGradient id="stone-wash" x1="0" y1="1" x2="1" y2="0">
          <stop offset="0" stop-color="var(--stone-lilac)"/>
          <stop offset="0.45" stop-color="var(--stone-blush)"/>
          <stop offset="0.75" stop-color="var(--stone-rose)"/>
          <stop offset="1" stop-color="var(--white)"/>
        </linearGradient>
      </defs>
      <rect width="380" height="180" fill="url(#stone-wash)"/>
    </svg>
  </section>

  <section class="card card-back">
    <div class="brand-circle"></div>
    <div class="brand-name">RV Bright Harbour</div>
  </section>

</body>
</html>
```